Velisto Promotions | Web Design Project

We need a web design for a new Promotion Company based in Toronto, Canada named Velisto Promotions.

Velisto Promotions has an idea and vision to set high standard, be EXCLUSIVE and attract a group of people that will follow us through events we promote (night clubs, brand promotions, music events, and sport events)

We want to present a high standards and classy image to the others...

layout/style of the website would be best explained by this template

http://www.quarnivex.com/view-ttemplate-58147.html

Target Market(s)

male/female age 25-40 Target: business owners young entrepreneur - clubing industry - media industry - promotion industry - marketing media industry

Industry/Entity Type

It Company

Requirements
Must have
• website would have about 5 pages ... example in terms of content (http://www.drubelworks.ca/lifestyle.html)

About Velisto
Events
Media
Promotions
Affiliates
Contact

as well as twitter and facebook logo/links
newsletter section
music control

need to have a easy to view gallery page (pictures from events)
Events would have to include flyers .. for past/future events
Media - would include videos/pictures from the events

Affiliates - list of affiliates with their logos and short description..

Main Pages
background would be pictures of Toronto
it would be nice to have some kind of flash/swf
space for flyer and picture of the week...

logo file is uploaded.

```html
<!DOCTYPE html>
<html lang="en">
<head>
<meta charset="utf-8">
<title>Velisto Promotions — Events</title>
<link href="https://fonts.googleapis.com/css2?family=Questrial&display=swap" rel="stylesheet">
<style>
  :root {
    --accent: #29a9e0;
    --accent-dark: #1b87c0;
    --ink: #ffffff;
    --ink-soft: #e6e6e6;
    --bar: rgba(0, 0, 0, 0.82);
    --panel: rgba(0, 0, 0, 0.55);
    --list: rgba(0, 0, 0, 0.6);
    --track: #777777;
    --thumb: #5a5a5a;
  }
  * { margin: 0; padding: 0; box-sizing: border-box; }
  html, body { width: 1200px; height: 750px; overflow: hidden; background: #0b0f16; }
  body { font-family: "Questrial", "Century Gothic", sans-serif; color: var(--ink); }

  .stage { position: relative; width: 1200px; height: 750px; overflow: hidden; }

  .city-backdrop {
    position: absolute; inset: 0;
    background:
      linear-gradient(180deg, rgba(58,92,150,0.85) 0%, rgba(34,52,86,0.7) 22%, rgba(18,22,30,0.9) 50%, rgba(28,22,18,0.95) 100%),
      linear-gradient(90deg, #2a2f38 0%, #1b2029 40%, #3a2c1e 85%, #5a3a18 100%);
  }

  /* top navigation */
  .top-bar {
    position: absolute; left: 0; top: 0; width: 1200px; height: 28px;
    background: var(--bar); display: flex; align-items: center;
  }
  .home-link { position: absolute; left: 9px; top: 5px; width: 17px; height: 16px; }
  .main-nav { position: absolute; left: 47px; top: 0; display: flex; gap: 24px; height: 28px; align-items: center; }
  .main-nav a { color: var(--ink); text-decoration: none; font-size: 18.5px; letter-spacing: 0.2px; text-transform: uppercase; }
  .player { position: absolute; left: 912px; top: 8px; display: flex; gap: 9px; }
  .player svg { width: 12px; height: 11px; }
  .now-playing {
    position: absolute; left: 1000px; top: 0; width: 200px; height: 28px;
    background: #000; font-size: 10.5px; line-height: 28px; padding-left: 5px;
    white-space: nowrap; overflow: hidden; color: var(--ink-soft);
  }

  /* content panel */
  .content-panel { position: absolute; left: 37px; top: 47px; width: 1125px; height: 656px; background: var(--panel); }
  .event-list { position: absolute; left: 89px; top: 63px; width: 1023px; height: 597px; background: var(--list); }

  .event { position: absolute; left: 98px; width: 1010px; height: 141px; }
  .event-flyer { position: absolute; left: 0; top: 0; width: 141px; height: 141px; }
  .event-title { position: absolute; left: 154px; top: -2px; font-size: 24px; font-weight: 400; color: var(--accent); letter-spacing: 0.2px; text-transform: uppercase; }
  .event-meta { position: absolute; left: 154px; top: 36px; font-size: 11.3px; line-height: 14px; color: var(--ink-soft); }
  .event-desc { position: absolute; left: 154px; top: 80px; width: 656px; font-size: 11.8px; line-height: 15.3px; color: var(--ink); white-space: nowrap; overflow: hidden; }
  .book-btn {
    position: absolute; left: 909px; top: 0; width: 94px; height: 23px;
    background: linear-gradient(180deg, #36b4ea, var(--accent-dark));
    font-size: 13px; line-height: 23px; text-align: center; color: #fff; text-decoration: none;
  }
  .book-btn-reflection {
    position: absolute; left: 909px; top: 24px; width: 94px; height: 23px;
    font-size: 13px; line-height: 23px; text-align: center; color: rgba(60,140,190,0.35);
    transform: scaleY(-1);
    background: linear-gradient(0deg, rgba(30,110,160,0.35), rgba(30,110,160,0));
  }

  .scroll-track { position: absolute; left: 1138px; top: 63px; width: 2px; height: 572px; background: var(--track); }
  .scroll-thumb { position: absolute; left: 1131px; top: 94px; width: 16px; height: 50px; background: var(--thumb); border: 1px solid #444; }

  .brand-mark { position: absolute; left: 916px; top: 647px; display: flex; align-items: center; gap: 8px; color: var(--accent); }
  .brand-mark .dot { width: 14px; height: 14px; border-radius: 50%; background: var(--accent); }
  .brand-name { font-size: 32px; line-height: 30px; letter-spacing: 1px; text-transform: uppercase; }
  .brand-sub { display: block; font-size: 9px; line-height: 10px; letter-spacing: 4px; text-align: right; }

  /* footer */
  .site-footer { position: absolute; left: 0; top: 722px; width: 1200px; height: 28px; background: var(--bar); }
  .legal { position: absolute; left: 9px; top: 0; line-height: 28px; font-size: 13.6px; text-transform: uppercase; color: var(--ink); }
  .legal a { color: var(--accent); text-decoration: none; }
  .social { position: absolute; right: 14px; top: 7px; display: flex; gap: 11px; }
  .social span { width: 15px; height: 15px; display: block; }
  .social .s1 { background: #e07a26; }
  .social .s2 { background: #3fa6d8; }
  .social .s3 { background: #3b5c9a; }
</style>
</head>
<body>
<div class="stage">
  <div class="city-backdrop" role="img" aria-label="Evening photograph of the Toronto downtown skyline"></div>

  <header class="top-bar">
    <svg class="home-link" viewBox="0 0 17 16" aria-label="Home"><path d="M8.5 1 L16 8 H13.5 V15 H10 V10.5 H7 V15 H3.5 V8 H1 Z" fill="#29a9e0"/></svg>
    <nav class="main-nav">
      <a href="#">About Velisto</a>
      <a href="#">Media</a>
      <a href="#">Events</a>
      <a href="#">Promotions</a>
      <a href="#">Affiliates</a>
      <a href="#">Contact</a>
    </nav>
    <div class="player" aria-label="Music controls">
      <svg viewBox="0 0 12 11"><rect x="1" y="1" width="2" height="9" fill="#fff"/><path d="M11 1 V10 L4 5.5 Z" fill="#fff"/></svg>
      <svg viewBox="0 0 12 11"><path d="M3 1 V10 L10 5.5 Z" fill="#fff"/></svg>
      <svg viewBox="0 0 12 11"><path d="M1 1 V10 L8 5.5 Z" fill="#fff"/><rect x="9" y="1" width="2" height="9" fill="#fff"/></svg>
      <svg viewBox="0 0 12 11"><rect x="1.5" y="1" width="9" height="9" fill="#fff"/></svg>
    </div>
    <div class="now-playing">Mira Solenne; Velvet Hour (Radio Edit).....</div>
  </header>

  <main class="content-panel"></main>
  <div class="event-list"></div>

  <article class="event" style="top:81px">
    <div class="event-flyer" role="img" aria-label="Event flyer: black and white crowd photo with red after-party banner" style="background:linear-gradient(180deg,#8a8a8a 0%,#3c3c3c 40%,#b0242c 55%,#7a7a7a 75%,#d8d8d8 100%)"></div>
    <h2 class="event-title">House Sounds of Toronto</h2>
    <p class="event-meta">Harbour Lounge / 42 Alder Row / Friday 25 Nov 2011 at 22:00h<br>Reservation &nbsp;/ +1 555-014-2290</p>
    <p class="event-desc">Lorem ipsum dolor sit amet, consetetur sadipscing elitr, sed diam nonumy eirmod tempor invidunt ut labore et dolore mag<br>erat, sed diam voluptua. At vero eos et accusam et justo duo dolores et ea rebum. Stet clita kasd gubergren, no sea takimat<br>Lorem ipsum dolor sit amet. Lorem ipsum dolor sit amet, consetetur sadipscing elitr, &nbsp;sed diam nonumy eirmod tempor invi<br>et dolore magna aliquyam erat, sed diam voluptua. At vero eos et accusam et justo duo dolores et ea</p>
    <a class="book-btn" href="#">BOOK NOW !</a>
    <div class="book-btn-reflection" aria-hidden="true">BOOK NOW !</div>
  </article>

  <article class="event" style="top:278px">
    <div class="event-flyer" role="img" aria-label="Event flyer: DJ in a suit against a blue sky backdrop" style="background:linear-gradient(160deg,#c7d3ea 0%,#6f86b8 45%,#3b4d7a 75%,#aab8d6 100%)"></div>
    <h2 class="event-title">House Sounds of Toronto</h2>
    <p class="event-meta">Harbour Lounge / 42 Alder Row / Friday 25 Nov 2011 at 22:00h<br>Reservation &nbsp;/ +1 555-014-2290</p>
    <p class="event-desc">Lorem ipsum dolor sit amet, consetetur sadipscing elitr, sed diam nonumy eirmod tempor invidunt ut labore et dolore mag<br>erat, sed diam voluptua. At vero eos et accusam et justo duo dolores et ea rebum. Stet clita kasd gubergren, no sea takimat<br>Lorem ipsum dolor sit amet. Lorem ipsum dolor sit amet, consetetur sadipscing elitr, &nbsp;sed diam nonumy eirmod tempor invi<br>et dolore magna aliquyam erat, sed diam voluptua. At vero eos et accusam et justo duo dolores et ea</p>
    <a class="book-btn" href="#">BOOK NOW !</a>
    <div class="book-btn-reflection" aria-hidden="true">BOOK NOW !</div>
  </article>

  <article class="event" style="top:476px">
    <div class="event-flyer" role="img" aria-label="Event flyer: golden club emblem on black" style="background:radial-gradient(circle at 50% 50%,#f4b51e 0%,#e09a10 38%,#0a0a0a 62%)"></div>
    <h2 class="event-title">House Sounds of Toronto</h2>
    <p class="event-meta">Harbour Lounge / 42 Alder Row / Friday 25 Nov 2011 at 22:00h<br>Reservation &nbsp;/ +1 555-014-2290</p>
    <p class="event-desc">Lorem ipsum dolor sit amet, consetetur sadipscing elitr, sed diam nonumy eirmod tempor invidunt ut labore et dolore mag<br>erat, sed diam voluptua. At vero eos et accusam et justo duo dolores et ea rebum. Stet clita kasd gubergren, no sea takimat<br>Lorem ipsum dolor sit amet. Lorem ipsum dolor sit amet, consetetur sadipscing elitr, &nbsp;sed diam nonumy eirmod tempor invi<br>et dolore magna aliquyam erat, sed diam voluptua. At vero eos et accusam et justo duo dolores et ea</p>
    <a class="book-btn" href="#">BOOK NOW !</a>
    <div class="book-btn-reflection" aria-hidden="true">BOOK NOW !</div>
  </article>

  <div class="scroll-track"></div>
  <div class="scroll-thumb"></div>

  <div class="brand-mark">
    <span class="dot"></span>
    <div>
      <span class="brand-name">Velisto</span>
      <span class="brand-sub">PROMOTIONS</span>
    </div>
  </div>

  <footer class="site-footer">
    <p class="legal">Copyright © 2011 Velisto. Use of this website constitutes acceptance of our <a href="#">User Agreement</a> and <a href="#">Privacy Policy</a>.</p>
    <div class="social" aria-label="Social links">
      <span class="s1"></span><span class="s2"></span><span class="s3"></span>
    </div>
  </footer>
</div>
</body>
</html>
```